Tidewell Consulting Schedule Of Rates

We need a brochure / proposal for our new company. Our company is a start up based in Australia who provides engineering and sales support to other renewable energy companies. Our brochure is a pitch-deck / sales item that catalogues our key services. We are engineering consultants.

Our website is www.tidewellpartners.com.au. Please review the website to get a feel of colour schemes etc.

We are looking for a strong, trustworthy feel, but the brochure also needs to be sales driven and to the point.

The second page that contains the $30 price point needs to be loud and clear.

The use of relevant icons throughout the document will be viewed favorably.

Please format the tables to look attractive.

The document will need to be in an editable format so content can be edited by us at a later date.

Please feel free to use the pics within the attached word document. The winning design will be provided with updated, clearer images upon request.

Thank you

Target Market(s)

Businesses that either sell or install solar PV and other renewable energy systems in Australia. Most of target market are likely to be electrical contractors.

Industry/Entity Type

Engineering

Colors
0255a3
0492cd
ffffff

Requirements
Must have
• Icons, graphics presentation, Clean and Clear, Business oriented. Sharp sales feel
Nice to have
• solar picture backgrounds maybe
Should not have
• cartoons, over sales driven,

```html
<!DOCTYPE html>
<html lang="en">
<head>
<meta charset="utf-8">
<title>Tidewell Consulting – About Us</title>
<link href="https://fonts.googleapis.com/css2?family=Barlow:wght@300;400&display=swap" rel="stylesheet">
<style>
  :root {
    --brand-deep: #0255a3;
    --brand-sky: #0492cd;
    --heading-blue: #1b7bc6;
    --paper: #ffffff;
    --ink: #2b2b2b;
    --backdrop: #e9ecef;
  }
  html, body {
    margin: 0;
    padding: 0;
    width: 1200px;
    height: 1200px;
    overflow: hidden;
    background: var(--backdrop);
    font-family: "Barlow", "Arial", sans-serif;
  }
  .page {
    position: absolute;
    left: 160px;
    top: 30px;
    width: 880px;
    height: 1140px;
    background: var(--paper);
    box-shadow: 0 6px 18px rgba(0,0,0,0.18);
  }
  .hero-photo {
    position: absolute;
    left: 0;
    top: 49px;
    width: 880px;
    height: 644px;
    background:
      radial-gradient(circle at 36% 30%, #ffffff 0%, #e6f2ff 8%, #8fc0f2 22%, rgba(58,120,210,0) 45%),
      linear-gradient(160deg, #3f7fd6 0%, #2a62c0 40%, #1f4fae 75%, #2d64c4 100%);
  }
  .about {
    position: absolute;
    left: 49px;
    top: 733px;
    width: 782px;
  }
  .about-title {
    margin: 0;
    font-weight: 400;
    font-size: 38px;
    line-height: 44px;
    color: var(--heading-blue);
    letter-spacing: 0.5px;
  }
  .about-rule {
    height: 0;
    border: 0;
    border-top: 1.5px solid var(--heading-blue);
    margin: 2px 0 0 0;
  }
  .about-columns {
    display: flex;
    justify-content: space-between;
    margin-top: 16px;
  }
  .about-column {
    width: 367px;
    font-size: 15.5px;
    line-height: 21px;
    font-weight: 400;
    color: var(--ink);
  }
  .about-column p {
    margin: 0 0 21px 0;
    text-align: justify;
  }
  .service-list {
    margin: 0;
    padding: 0;
    list-style: none;
  }
  .service-list li {
    position: relative;
    padding-left: 21px;
    text-align: justify;
  }
  .service-list li::before {
    content: "•";
    position: absolute;
    left: 0;
  }
</style>
</head>
<body>
  <main class="page">
    <div class="hero-photo" role="img" aria-label="Close-up photograph of blue solar panels reflecting bright sunlight against a blue sky"></div>

    <section class="about">
      <h1 class="about-title">ABOUT US</h1>
      <hr class="about-rule">
      <div class="about-columns">
        <div class="about-column">
          <p>Our team of renewable energy experts specialise in project development, feasibility studies, system design and delivery. We have successfully delivered over 40MW of commercial and utility renewable energy systems; our team has proven capability in this space.</p>
          <p>With our in-house team of engineers, designers, and business analysts, the Tidewell Consulting team has the expertise and dedication to provide your business with a superior design solution.</p>
          <p>We utilize our real-life experience, industry leading software and trusted industry partners to provide an optimum and cost effective energy solution for our customers.</p>
        </div>
        <div class="about-column">
          <p>Some of the key services we offer in this area are:</p>
          <ul class="service-list" style="margin-top:-21px;">
            <li>Grid tied and off-grid renewable energy design.</li>
            <li>Battery Storage design and integration.</li>
            <li>Energy data analysis and modelling</li>
            <li>DNSP and other relevant approvals</li>
            <li>Electrical Installation Design</li>
          </ul>
        </div>
      </div>
    </section>
  </main>
</body>
</html>
```